Quillorah

Business cards and core flute signage. The business is only in its infant as a 'market' business. I would like the name to be curved across the page in different colours with a bold line underneath finished with an exotic pen drawing the line. (Similar to pictures)
We are trying to reach all markets as they are designer pens and items are made as requested or they can select from already manufactured pens on display.
I have included some images of the actual pens that I make for inspiration, we are very open to your ideas and guidance if you have a specific design in mind.
If you would more pen photo options, please contact me with your email details.
Derek Malthby
Pen Maker & Wood Turner
Ph. 0431 206 548
Target Market(s)
Generally professional customers who would use a pen for work on a daily basis
Industry/Entity Type
Business
Requirements
Must have
- Punchy and catchy styling
Nice to have
- One of my pens

```html
<!DOCTYPE html>
<html lang="en">
<head>
<meta charset="utf-8">
<title>Quillorah – Business Card</title>
<link rel="stylesheet" href="https://fonts.googleapis.com/css2?family=Lato:wght@400;700&family=Dosis:wght@500&display=swap">
<style>
  :root {
    --backdrop: #e9e6e1;
    --card-white: #fbfbfb;
    --brand-red: #e0202c;
    --accent-yellow: #f3d400;
    --text-light: #ffffff;
    --text-soft: #ffd9db;
    --logo-ink: #d6323c;
  }
  * { margin: 0; padding: 0; box-sizing: border-box; }
  html, body {
    width: 1200px; height: 1023px; overflow: hidden;
    background: var(--backdrop);
  }
  .stage {
    width: 1200px; height: 1023px;
    display: flex; align-items: center; justify-content: center;
  }
  .card {
    position: relative;
    width: 900px; height: 514px;
    background: var(--card-white);
    box-shadow: 0 18px 40px rgba(0,0,0,0.22);
    overflow: hidden;
  }
  .card-wave { position: absolute; inset: 0; width: 100%; height: 100%; }
  .brand {
    position: absolute; left: 40px; top: 290px;
    font-family: "Dosis", sans-serif;
  }
  .brand-name {
    display: flex; align-items: center; gap: 10px;
    font-size: 48px; font-weight: 500; letter-spacing: 3px;
    color: var(--logo-ink); text-transform: uppercase; line-height: 1;
  }
  .brand-dot {
    width: 12px; height: 12px; border-radius: 50%;
    background: var(--logo-ink);
  }
  .brand-tagline {
    margin-top: 12px;
    font-size: 21px; letter-spacing: 1px; color: var(--logo-ink);
  }
  .contact {
    position: absolute; left: 600px; top: 250px;
    font-family: "Lato", sans-serif; color: var(--text-light);
  }
  .contact-name { font-size: 30px; font-weight: 700; }
  .contact-role { font-size: 18px; color: var(--text-soft); margin-top: 4px; }
  .contact-list { list-style: none; margin-top: 62px; }
  .contact-list li {
    display: flex; align-items: center; gap: 12px;
    font-size: 19px; line-height: 1.55;
  }
  .contact-icon { width: 18px; height: 18px; flex: none; }
</style>
</head>
<body>
<main class="stage">
  <article class="card">
    <svg class="card-wave" viewBox="0 0 900 514" aria-hidden="true">
      <path d="M700 0 C670 120 630 250 570 262 C520 272 510 130 460 130 C410 130 400 330 430 514 L900 514 L900 0 Z"
            fill="none" stroke="var(--accent-yellow)" stroke-width="14"/>
      <path d="M700 0 C670 120 630 250 570 262 C520 272 510 130 460 130 C410 130 400 330 430 514 L900 514 L900 0 Z"
            fill="var(--brand-red)"/>
    </svg>

    <div class="brand">
      <div class="brand-name"><span>Quillorah</span><span class="brand-dot"></span></div>
      <div class="brand-tagline">Custom Hand Made Pens</div>
    </div>

    <section class="contact">
      <h1 class="contact-name">Derek Malthby</h1>
      <p class="contact-role">Pen Maker &amp; Wood Turner</p>
      <ul class="contact-list">
        <li>
          <svg class="contact-icon" viewBox="0 0 24 24"><path fill="#fff" d="M6.6 10.8a15 15 0 0 0 6.6 6.6l2.2-2.2c.3-.3.7-.4 1-.2 1.1.4 2.3.6 3.6.6.6 0 1 .4 1 1V20c0 .6-.4 1-1 1C10.6 21 3 13.4 3 4c0-.6.4-1 1-1h3.5c.6 0 1 .4 1 1 0 1.3.2 2.5.6 3.6.1.3 0 .7-.2 1z"/></svg>
          0431 206 548
        </li>
        <li>
          <svg class="contact-icon" viewBox="0 0 24 24"><path fill="#fff" d="M3 5h18v14H3z"/><path fill="none" stroke="var(--brand-red)" stroke-width="1.8" d="M3 5l9 7 9-7"/></svg>
          info@quillorahpens.com
        </li>
        <li>
          <svg class="contact-icon" viewBox="0 0 24 24"><circle cx="12" cy="12" r="9" fill="none" stroke="#fff" stroke-width="2"/><path fill="none" stroke="#fff" stroke-width="1.6" d="M3 12h18M12 3c3 3 3 15 0 18M12 3c-3 3-3 15 0 18"/></svg>
          www.quillorahpens.com
        </li>
      </ul>
    </section>
  </article>
</main>
</body>
</html>
```